Business Card for TOV

We need a Corporate style business card for a new Industrial recycling company based in Australia. We recycle industrial products from Mining companies, power stations and other large industry all around the country.

We want the card to represent a modern, innovative professional company that is an industry leader.

We want the card to be double sided. I think with the logo centred by itself on one side and the text displayed with all our details on the other side.

(or you could put the persons name with the job title on the side with the logo?? I'll leave that up to your creative sides)

Open to how you divide and place the information on the one side of the card.

I think the persons name and the title should have its own place. The rest of the information can be placed as you think is best and then I will provide feedback as to what I think works best.

I have attached the logo file so you can add that to the one side. Whether you use it in a smaller form on the second side too is an option but I'll leave that up to you initially?

Information required on the card is as follows

Dermot Halloran
Director

0438 972 506

dermot@tovq.com.au

Po Box 782
Brindle ACT 2694

www.tovq.com.au

ACN 582 917 306 (This can be in very small print and can be in the bottom corner of the card or somewhere not very prominent

Wanted to thank everyone for their submissions. 

We were really torn on about 5 designs in the end.

We decided to go with the first one we liked.

We have another company that is going to need logo and business card design in the coming weeks.

I will save your designer ID's so I can invite you all to that project. too!

Thanks again and all the best

Dermot

Target Market(s)

Corporate and medium to large business clients

Industry/Entity Type

Industrial

```html
<!DOCTYPE html>
<html lang="en">
<head>
<meta charset="utf-8">
<title>Tovara Industrial Recovery – Business Card</title>
<link rel="stylesheet" href="https://fonts.googleapis.com/css2?family=Arimo:wght@400;700&display=swap">
<style>
  :root {
    --stage: #ecebe7;
    --green-deep: #1f4a12;
    --green-mid: #3f7d1e;
    --green-bright: #7cbf2e;
    --green-accent: #6fb52b;
    --ink: #1c1c1c;
    --blue: #1f6fa8;
    --paper: #ffffff;
    --mist: #eef4ea;
  }
  * { box-sizing: border-box; margin: 0; padding: 0; }
  html, body {
    width: 1200px; height: 784px; overflow: hidden;
    background: var(--stage);
    font-family: "Arimo", Arial, sans-serif;
  }
  .stage {
    width: 1200px; height: 784px;
    display: flex; align-items: center; justify-content: center; gap: 60px;
  }
  .card {
    position: relative;
    width: 520px; height: 318px;
    border-radius: 4px;
    overflow: hidden;
    box-shadow: 0 10px 28px rgba(0,0,0,.18), 0 2px 6px rgba(0,0,0,.12);
  }

  /* Front side */
  .card--front {
    background: radial-gradient(ellipse at 30% 60%, var(--green-bright) 0%, var(--green-mid) 45%, var(--green-deep) 100%);
  }
  .card--front .pattern {
    position: absolute; inset: 0;
    background: radial-gradient(ellipse at 70% 35%, rgba(140,200,80,.35) 0%, rgba(140,200,80,0) 60%);
  }
  .front-brand {
    position: absolute; left: 50%; top: 50%;
    transform: translate(-50%, -50%);
    display: flex; align-items: center; gap: 22px;
  }
  .brand-mark {
    width: 74px; height: 74px; border-radius: 50%;
    background: var(--green-accent);
    flex: none;
  }
  .card--front .brand-mark { background: #ffffff; opacity: .9; }
  .front-brand .brand-name {
    font-weight: 700; font-size: 30px; line-height: 1.1;
    letter-spacing: 1px; text-transform: uppercase;
    color: #ffffff;
  }

  /* Back side */
  .card--back {
    background: linear-gradient(90deg, var(--paper) 0%, var(--paper) 62%, var(--mist) 100%);
  }
  .back-brand {
    position: absolute; left: 34px; top: 34px;
    display: flex; align-items: center; gap: 16px;
  }
  .back-brand .brand-mark { width: 58px; height: 58px; }
  .back-brand .brand-name {
    font-weight: 700; font-size: 22px; line-height: 1.1;
    letter-spacing: .8px; text-transform: uppercase;
    color: var(--ink);
  }
  .person {
    position: absolute; left: 40px; top: 140px;
  }
  .person-name { font-weight: 700; font-size: 18px; color: var(--ink); }
  .person-title { font-size: 13px; color: var(--green-accent); margin-top: 4px; }

  .contact-list {
    position: absolute; left: 40px; top: 196px;
    list-style: none;
    font-size: 15px; line-height: 20px; color: var(--ink);
  }
  .contact-list li { display: flex; align-items: flex-start; gap: 7px; }
  .contact-list svg { width: 15px; height: 15px; margin-top: 3px; flex: none; }
  .contact-list .indent { padding-left: 22px; }

  .acn {
    position: absolute; right: 28px; top: 196px;
    font-size: 10px; color: var(--ink);
  }
</style>
</head>
<body>
<main class="stage">

  <section class="card card--front" aria-label="Card front">
    <div class="pattern" role="img" aria-label="Green background with rows of soft oval dots"></div>
    <div class="front-brand">
      <span class="brand-mark" aria-hidden="true"></span>
      <span class="brand-name">Tovara<br>Industrial Recovery</span>
    </div>
  </section>

  <section class="card card--back" aria-label="Card back">
    <div class="back-brand">
      <span class="brand-mark" aria-hidden="true"></span>
      <span class="brand-name">Tovara<br>Industrial Recovery</span>
    </div>

    <div class="person">
      <p class="person-name">Dermot Halloran</p>
      <p class="person-title">Director</p>
    </div>

    <ul class="contact-list">
      <li>
        <svg viewBox="0 0 16 16" aria-hidden="true"><path fill="#6fb52b" d="M3.5 1.5l2.5 0 1 3.5-1.6 1.2a8 8 0 0 0 4.4 4.4L11 9l3.5 1v2.5c0 1-1 2-2 2A11 11 0 0 1 1.5 3.5c0-1 1-2 2-2z"/></svg>
        <span>0438 972 506</span>
      </li>
      <li>
        <svg viewBox="0 0 16 16" aria-hidden="true"><rect x="1" y="3.5" width="14" height="9.5" rx="1" fill="#6fb52b"/><path d="M1.5 4.2L8 9l6.5-4.8" fill="none" stroke="#fff" stroke-width="1.3"/></svg>
        <span>dermot@tovq.com.au</span>
      </li>
      <li>
        <svg viewBox="0 0 16 16" aria-hidden="true"><circle cx="8" cy="8" r="6.8" fill="#6fb52b"/><g fill="none" stroke="#fff" stroke-width="1"><ellipse cx="8" cy="8" rx="3" ry="6.8"/><path d="M1.2 8h13.6M2.4 4.8h11.2M2.4 11.2h11.2"/></g></svg>
        <span>www.tovq.com.au</span>
      </li>
      <li>
        <svg viewBox="0 0 16 16" aria-hidden="true"><path fill="#6fb52b" d="M8 1.5l7 6.2h-2.2V14.5H9.7v-4H6.3v4H3.2V7.7H1z"/></svg>
        <span>Po Box 782</span>
      </li>
      <li class="indent">Brindle ACT 2694</li>
    </ul>

    <p class="acn">ACN 582 917 306</p>
  </section>

</main>
</body>
</html>
```